HarmoNest Ensemble Jubilee
Date: Sunday Oct 2, 2022
When: 2-4 p.m.
Location: Brindle9 Alehouse
413 Marlowe Ct #200, Sacramento, CA 95821
Tickets: www.Tixolvo.com
General seating: $15 for adults and $10 for students

```html
<!DOCTYPE html>
<html lang="en">
<head>
<meta charset="utf-8">
<title>HarmoNest Ensemble Jubilee</title>
<link rel="stylesheet" href="https://fonts.googleapis.com/css2?family=Marcellus&family=Roboto:wght@400;500;700;900&display=swap">
<style>
  :root {
    --backdrop: #b57cf5;
    --flyer-deep: #2c1a52;
    --flyer-mid: #4a2478;
    --flyer-plum: #5e2a8c;
    --band: rgba(30, 18, 70, 0.45);
    --bubble: rgba(150, 80, 190, 0.55);
    --bubble-soft: rgba(170, 90, 200, 0.35);
    --pin: rgba(160, 60, 170, 0.4);
    --pin-core: rgba(50, 25, 95, 0.55);
    --ink: #ffffff;
    --ink-muted: rgba(200, 170, 230, 0.55);
  }
  * { margin: 0; padding: 0; box-sizing: border-box; }
  html, body { width: 1200px; height: 960px; overflow: hidden; }
  body { background: var(--backdrop); position: relative; font-family: "Roboto", sans-serif; }

  .flyer {
    position: absolute; left: 280px; top: 27px; width: 640px; height: 906px;
    background: linear-gradient(160deg, var(--flyer-deep) 0%, var(--flyer-mid) 45%, var(--flyer-plum) 75%, var(--flyer-deep) 100%);
    overflow: hidden; color: var(--ink);
    box-shadow: 0 12px 30px rgba(40, 10, 80, 0.35);
  }
  .flyer-shapes { position: absolute; inset: 0; }

  .title-block { position: absolute; left: 0; top: 150px; width: 640px; text-align: center; }
  .title-kicker { font-family: "Marcellus", serif; font-size: 24px; letter-spacing: 5px; text-transform: uppercase; }
  .title-main { font-family: "Marcellus", serif; font-size: 100px; line-height: 1; margin-top: 14px; }

  .info-label {
    position: absolute; font-size: 14px; letter-spacing: 3px; text-transform: uppercase;
    color: var(--ink-muted); font-weight: 500; transform: rotate(-90deg); transform-origin: left top;
  }
  .date-text { position: absolute; left: 112px; top: 382px; width: 180px; text-align: center; font-weight: 700; line-height: 1.05; }
  .date-day { font-size: 22px; }
  .date-weekday { font-size: 44px; font-weight: 900; }
  .date-year { font-size: 24px; }
  .time-text { position: absolute; left: 320px; top: 420px; font-size: 28px; font-weight: 700; }
  .time-text small { font-size: 20px; font-weight: 500; }

  .venue-text { position: absolute; left: 205px; top: 580px; font-size: 22px; line-height: 1.25; }
  .venue-name { font-weight: 700; font-size: 23px; }

  .tickets { position: absolute; right: 24px; top: 770px; text-align: right; }
  .tickets-line {
    display: inline-block; background: var(--band); padding: 6px 12px;
    font-size: 24px; font-weight: 700;
  }
  .tickets-line span { letter-spacing: 3px; font-weight: 500; }
  .tickets-price { margin-top: 8px; font-size: 19px; font-weight: 700; }
  .tickets-price strong { font-size: 34px; font-weight: 900; }
</style>
</head>
<body>
  <div class="flyer">
    <svg class="flyer-shapes" width="640" height="906" viewBox="0 0 640 906">
      <defs>
        <radialGradient id="mic-tone" cx="40%" cy="40%" r="70%">
          <stop offset="0%" stop-color="#5b2c90"/>
          <stop offset="100%" stop-color="#2a1450"/>
        </radialGradient>
      </defs>
      <rect x="0" y="120" width="640" height="230" fill="var(--band)"/>
      <circle cx="560" cy="230" r="40" fill="var(--bubble-soft)"/>
      <circle cx="575" cy="188" r="18" fill="var(--bubble-soft)"/>
      <g role="img" aria-label="Close-up of a stage microphone grille">
        <circle cx="600" cy="560" r="190" fill="url(#mic-tone)"/>
      </g>
      <path d="M300 475 a175 175 0 0 1 124 299 L300 895 L176 774 A175 175 0 0 1 300 475 Z" fill="var(--pin)"/>
      <circle cx="300" cy="645" r="130" fill="var(--pin-core)"/>
      <circle cx="200" cy="445" r="120" fill="var(--bubble)"/>
      <circle cx="375" cy="440" r="82" fill="var(--bubble-soft)"/>
    </svg>

    <div class="title-block">
      <div class="title-kicker">HarmoNest Ensemble</div>
      <div class="title-main">Jubilee</div>
    </div>

    <div class="info-label" style="left:100px; top:470px;">Date</div>
    <div class="date-text">
      <div class="date-day">Oct 2</div>
      <div class="date-weekday">SUNDAY</div>
      <div class="date-year">2022</div>
    </div>

    <div class="info-label" style="left:300px; top:475px;">When</div>
    <div class="time-text">2-4 <small>p.m.</small></div>

    <div class="info-label" style="left:180px; top:720px;">Location</div>
    <div class="venue-text">
      <div class="venue-name">Brindle9 Alehouse</div>
      <div>413 Marlowe Ct</div>
      <div>#200, Sacramento,</div>
      <div>CA 95821</div>
    </div>

    <div class="tickets">
      <div class="tickets-line"><span>TICKETS:</span> www.Tixolvo.com</div>
      <div class="tickets-price"><strong>$15</strong> for adults and <strong>$10</strong> for students</div>
    </div>
  </div>
</body>
</html>
```